Build a Web page - Dovin Pratchell Homes, LLC - a custom home builder

We are a custom home builder in Wisconsin. Need a basic web page with a home page, About Us, Contact info, Gallery, and Testimonials page. Gallery will probably have sub-pages and each will have about ten pictures or less. I already own the domain and have web hosting through Wix, I just need the site built. Once the page is built I should be able to do the upkeep on it myself. If I need to add pictures or whatever.
Updates

Project Deadline Extended
Reason: I am still looking through designs and will select soon - thank you!

Target Market(s)

Gen X and Millennials who are looking to build a home. Custom built homes - not generic spec homes.

Industry/Entity Type

Home Builder

Number of Pages Required

5+ page

Font styles to use
Sans Serif

Colors
ffffff
ec1f27
000000
9d9d9d

Requirements
Must have
• I have no idea if I want coded or in coded. I'm not sure of the difference and why I would want one over the other.
Nice to have
• We like the following colors - red, black, gray, white.
Should not have
• not a big fan of clip art like hammers, tape measures, etc. Must look professional.

```html
<!DOCTYPE html>
<html lang="en">
<head>
<meta charset="utf-8">
<title>Dovin Pratchell Homes, LLC</title>
<link rel="stylesheet" href="https://fonts.googleapis.com/css2?family=Raleway:wght@400;500;600;700&family=Open+Sans:wght@400;600;700&display=swap">
<style>
:root{
  --red:#a8201f;
  --red-bright:#c4262b;
  --ink:#111111;
  --grey:#6f6f6f;
  --grey-light:#ededed;
  --grey-mid:#9d9d9d;
  --white:#ffffff;
  --footer:#262626;
  --footer-base:#1c1c1c;
  --quote:#eceff3;
  --text:#444444;
}
*{margin:0;padding:0;box-sizing:border-box}
html,body{width:1200px;height:2769px;overflow:hidden}
body{position:relative;background:var(--white);font-family:"Open Sans",Arial,sans-serif;color:var(--text)}
.abs{position:absolute}

/* top bar */
.topbar{left:0;top:0;width:1200px;height:50px;background:var(--white)}
.topbar .ask{left:60px;top:13px;display:flex;align-items:center;gap:8px;font-size:15px}
.topbar .ask b{color:var(--red-bright);font-weight:700}
.topbar .ask span{color:#333}
.social{display:flex;gap:6px}
.social i{display:block;width:24px;height:24px;border:1.5px solid #555;border-radius:50%}
.topbar .social{left:994px;top:12px}

/* nav */
.nav{left:0;top:50px;width:1200px;height:46px;background:var(--red)}
.nav ul{position:absolute;top:0;height:46px;display:flex;list-style:none}
.nav li{height:46px;line-height:46px;padding:0 17px;color:var(--white);font-weight:600;font-size:14px;text-transform:uppercase}
.nav li.active{background:#8d8d8d}
.nav .left{left:61px}
.nav .right{left:664px}
.brand{left:550px;top:22px;width:112px;height:108px;background:var(--white);box-shadow:0 0 0 3px #b5b5b5 inset;display:flex;align-items:center;justify-content:center;text-align:center;z-index:5}
.brand span{font-family:"Raleway",sans-serif;font-weight:700;font-size:13px;line-height:1.3;color:var(--ink);letter-spacing:.5px}

/* hero */
.hero{left:0;top:96px;width:1200px;height:526px;background:linear-gradient(180deg,#7aa2d0 0%,#b8cde2 30%,#8d8f86 48%,#6f7d64 62%,#5d8a38 80%,#4a7a2c 100%)}
.hero .kicker{left:0;top:164px;width:1200px;text-align:center}
.hero .kicker span{display:inline-block;white-space:nowrap;padding:0 14px;height:36px;background:rgba(120,120,120,.7);color:var(--white);font-family:"Raleway",sans-serif;font-weight:500;font-size:21px;line-height:36px;letter-spacing:.3px}
.hero h1{left:0;top:204px;width:1200px;text-align:center;color:var(--white);font-family:"Raleway",sans-serif;font-weight:700;font-size:56px;line-height:70px;letter-spacing:1px;text-shadow:0 2px 6px rgba(0,0,0,.35)}
.btn-red{background:var(--red);color:var(--white);font-weight:700;font-size:14px;text-transform:uppercase;text-align:center}
.hero .btn-red{left:516px;top:288px;width:166px;height:42px;line-height:42px}

/* about */
.about{left:0;top:622px;width:1200px;height:1276px;background:var(--grey-light)}
.section-title{width:1200px;left:0;text-align:center;font-family:"Raleway",sans-serif;font-weight:600;font-size:40px;color:var(--ink)}
.rule{left:548px;width:104px;height:2px;background:#555}
.about .lead{left:0;top:174px;width:1200px;text-align:center;color:var(--red);font-size:19px}
.about .body{left:100px;top:228px;width:1000px;text-align:center;font-size:14.5px;line-height:28px;color:#333}
.wave{left:0;top:652px;width:1200px;height:624px}
.card{top:391px;width:318px;height:414px;background:var(--white);box-shadow:0 1px 4px rgba(0,0,0,.18);z-index:3}
.card .photo{position:absolute;left:8px;top:10px;width:302px;height:142px}
.card .cap{position:absolute;left:8px;top:152px;width:302px;height:40px;background:var(--grey);color:var(--white);font-size:17px;line-height:40px;padding-left:14px;white-space:nowrap}
.card p{position:absolute;left:20px;width:280px;font-size:13px;line-height:21px;color:#333}
.card .more{position:absolute;right:22px;bottom:14px;color:#1c3a8a;font-size:13.4px}
.card .green{color:#3a9a2a}
.banner-sub{left:0;top:953px;width:1200px;text-align:center;color:var(--white);font-family:"Raleway",sans-serif;font-size:33px}
.banner-title{left:0;top:1010px;width:1200px;text-align:center;color:var(--white);font-family:"Raleway",sans-serif;font-weight:700;font-size:38px}
.btn-grey{left:495px;top:1087px;width:299px;height:67px;background:#7a7a7a;color:var(--white);font-family:"Raleway",sans-serif;font-size:25px;line-height:67px;text-align:center;border-radius:3px}

/* testimonials */
.quote{top:2119px;width:517px;height:115px;background:var(--quote);padding:14px 24px;font-size:13.5px;line-height:23px;color:#666}
.avatar{top:2210px;width:92px;height:92px;border-radius:50%;border:4px solid var(--white);background:radial-gradient(circle at 50% 40%,#c9a58a 0%,#8a6a55 55%,#3d4a66 100%)}
.who{top:2246px;font-size:13.5px}
.who b{display:block;color:#222;font-weight:600}
.who span{display:block;color:#888;margin-top:8px}

/* footer */
.footer{left:0;top:2374px;width:1200px;height:355px;background:var(--footer);color:#9a9a9a;font-size:13px}
.footer .logo{left:105px;top:42px;width:113px;height:102px;border:3px solid #9a9a9a;display:flex;align-items:center;justify-content:center;text-align:center;font-family:"Raleway",sans-serif;font-weight:700;font-size:12px;line-height:1.35;color:#cfcfcf}
.footer .about-text{left:60px;top:174px;width:240px;line-height:20px}
.footer .about-text b{color:#cfcfcf;font-weight:600}
.footer .social{left:60px;top:256px}
.footer .social i{width:28px;height:28px;border:none;background:#555}
.footer h4{top:40px;color:var(--white);font-size:13.5px;font-weight:700;text-transform:uppercase;letter-spacing:.5px}
.contact-list{left:334px;top:80px;list-style:none}
.contact-list li{display:flex;gap:12px;line-height:20px;margin-bottom:9px;font-size:12.5px}
.contact-list svg{flex:none;margin-top:3px}
.info-list{left:633px;top:82px;list-style:none}
.info-list li{line-height:35px}
.info-list li::before{content:"›";color:var(--red-bright);margin-right:10px;font-weight:700}
.news-text{left:890px;top:80px;width:250px;line-height:28px}
.field{left:890px;top:175px;width:249px;height:46px;border:1px solid #555;color:#bbb;padding-left:20px;line-height:44px}
.footer .btn-red{left:890px;top:238px;width:249px;height:48px;line-height:48px}
.base{left:0;top:2729px;width:1200px;height:40px;background:var(--footer-base);color:#bbb;font-size:13px;line-height:40px;text-align:center}
</style>
</head>
<body>

<header class="abs topbar">
  <div class="abs ask">
    <svg width="20" height="20" viewBox="0 0 20 20"><circle cx="10" cy="10" r="9" fill="none" stroke="#c4262b" stroke-width="1.6"/><path d="M7 5.5l2 2-1 1.3c.6 1.3 1.6 2.3 2.9 2.9l1.3-1 2 2-1.3 1.4C9.8 14 6 10.2 5.8 6.8z" fill="#c4262b"/></svg>
    <b>Any Questions</b><span>Call us now on 1300 555 018</span>
  </div>
  <div class="abs social"><i></i><i></i><i></i><i></i><i></i></div>
</header>

<nav class="abs nav">
  <ul class="left"><li class="active">Home</li><li>About Us</li><li>Services</li><li>Projects</li><li>Pages</li></ul>
  <ul class="right"><li>Blog</li><li>FAQ</li><li>Gallery</li><li>Blog</li><li>Contact Us</li></ul>
</nav>
<div class="abs brand"><span>DOVIN<br>PRATCHELL<br>HOMES</span></div>

<section class="abs hero" role="img" aria-label="Photo of a two-storey family home with stone front, garage and green lawn under a blue sky">
  <div class="abs kicker"><span>LOREM IPSUM DOLOR SIT AMET, CONSECTETUER</span></div>
  <h1 class="abs">DOVIN PRATCHELL HOMES</h1>
  <div class="abs btn-red">Tell me more</div>
</section>

<section class="abs about">
  <h2 class="abs section-title" style="top:68px">About Dovin Pratchell Homes</h2>
  <div class="abs rule" style="top:138px"></div>
  <p class="abs lead">Hollister Build, Inc specializes in building High Performance Homes in Alder County Wisconsin.</p>
  <p class="abs body">As a GreenMark Partner, we have constructed many GreenMark homes and even developed Alder County's first GreenMark subdivision on Juniper Lane, in Fernhill WI. We have also built many High Performance Homes in the beautiful Willow Ridge Estates subdivision. Hollister Build, Inc is a registered builder and member of the Alder County Home Builders Association.</p>

  <svg class="abs wave" viewBox="0 0 1200 624" preserveAspectRatio="none" role="img" aria-label="Photo of a row of suburban houses under a red tint">
    <defs>
      <linearGradient id="redTint" x1="0" y1="0" x2="0" y2="1">
        <stop offset="0" stop-color="#b83a36"/>
        <stop offset=".45" stop-color="#a9312f"/>
        <stop offset="1" stop-color="#a32523"/>
      </linearGradient>
    </defs>
    <path d="M0 70 C 300 10, 720 -14, 1200 22 L1200 624 L0 624 Z" fill="url(#redTint)"/>
  </svg>

  <article class="abs card" style="left:59px">
    <div class="photo" role="img" aria-label="Photo of a smiling man in a shirt standing in a bright office" style="background:linear-gradient(135deg,#9c7a5a,#d8c3a8 55%,#6e6a78)"></div>
    <div class="cap">What is a High Performance Home?</div>
    <p style="top:206px">High Performance Homes have increased comfort and efficiency and are beautiful on the inside and out. They save energy, conserve water, are more durable, cost less to maintain, are healthier for the occupants and are less stressful on the environment.<br><span class="green">Simply put, they are better homes!</span></p>
    <span class="more">Read More[+]</span>
  </article>

  <article class="abs card" style="left:441px">
    <div class="photo" role="img" aria-label="Photo of a timber house frame under construction" style="background:linear-gradient(160deg,#e8e3dc 0%,#c9956a 45%,#9a5a34 100%)"></div>
    <div class="cap">View a High Performance Home</div>
    <p style="top:206px">We are very proud of our beautiful High Performance Homes and want everyone to experience the comfort and efficiency.<br><br>Contact Hollister Build and we will gladly schedule a viewing of one of our High Performance Homes located in the scenic Willow Ridge Estates in Fernhill, Wisconsin.</p>
    <span class="more">Read More[+]</span>
  </article>

  <article class="abs card" style="left:823px">
    <div class="photo" role="img" aria-label="Photo of a builder in a hard hat on a steel frame site" style="background:linear-gradient(150deg,#9fb8d0 0%,#5e6b7e 50%,#2f3a4a 100%)"></div>
    <div class="cap">Buy or Build a High Performance</div>
    <p style="top:202px">Your dream home is waiting and it is a Hollister Build High Performance Home!<br><br>See all the beautiful and affordable High Performance Homes that Hollister Build currently has for sale or contact us for more information about how Hollister Build can build your own custom High Performance Dream Home.</p>
    <span class="more">Read More[+]</span>
  </article>

  <p class="abs banner-sub">Successfully Delivering Projects</p>
  <h2 class="abs banner-title">Buy or Build a High Performance Home</h2>
  <div class="abs btn-grey">Contact Information ›</div>
</section>

<section>
  <h2 class="abs section-title" style="top:1979px">Client Testimonials</h2>
  <div class="abs rule" style="top:2051px"></div>

  <blockquote class="abs quote" style="left:63px">We have several sites now built in Corvane across several servers and have had almost zero issues. The documentation is great and the feature set is phenomenal...</blockquote>
  <div class="abs avatar" role="img" aria-label="Portrait photo of client Owen Halberg" style="left:72px"></div>
  <div class="abs who" style="left:191px"><b>Owen Halberg</b><span>Northfield Company CEO</span></div>

  <blockquote class="abs quote" style="left:598px">We have several sites now built in Corvane across several servers and have had almost zero issues. The documentation is great and the feature set is phenomenal...</blockquote>
  <div class="abs avatar" role="img" aria-label="Portrait photo of client Lena Marsh" style="left:608px;background:radial-gradient(circle at 50% 40%,#d8b39a 0%,#6b4a3c 55%,#2e2a30 100%)"></div>
  <div class="abs who" style="left:726px"><b>Lena Marsh</b><span>Northfield Company CEO</span></div>
</section>

<footer class="abs footer">
  <div class="abs logo">DOVIN<br>PRATCHELL<br>HOMES</div>
  <p class="abs about-text"><b>Dovin Pratchell Homes</b> is a registered builder and member of the Alder County Home Builders Association.</p>
  <div class="abs social"><i></i><i></i><i></i><i></i></div>

  <h4 class="abs" style="left:336px">Get in touch</h4>
  <ul class="abs contact-list">
    <li><svg width="12" height="14" viewBox="0 0 12 14"><path d="M6 0C2.8 0 .5 2.3.5 5.3 .5 9 6 14 6 14s5.5-5 5.5-8.7C11.5 2.3 9.2 0 6 0zm0 7.5a2.2 2.2 0 110-4.4 2.2 2.2 0 010 4.4z" fill="#c4262b"/></svg><span>88 Harbor Lane, Lakeview, WI 53001<br>United States</span></li>
    <li style="margin-top:8px"><svg width="12" height="12" viewBox="0 0 12 12"><path d="M2 0l3 3-1.4 1.6c.8 1.6 2.2 3 3.8 3.8L9 7l3 3-1.8 2C5 11.6.4 7 0 1.8z" fill="#c4262b"/></svg><span>(123) 555-0147</span></li>
    <li style="margin-top:8px"><svg width="13" height="10" viewBox="0 0 13 10"><rect x=".6" y=".6" width="11.8" height="8.8" fill="none" stroke="#c4262b" stroke-width="1.2"/><path d="M.6.6l5.9 5 5.9-5" fill="none" stroke="#c4262b" stroke-width="1.2"/></svg><span>info@dovinpratchell.com</span></li>
    <li style="margin-top:8px"><svg width="12" height="12" viewBox="0 0 12 12"><circle cx="6" cy="6" r="5.3" fill="none" stroke="#c4262b" stroke-width="1.2"/><path d="M6 3v3.3l2.2 1.4" fill="none" stroke="#c4262b" stroke-width="1.2"/></svg><span>Mon - Sat: 9:00 - 18:00</span></li>
  </ul>

  <h4 class="abs" style="left:633px">Information</h4>
  <ul class="abs info-list"><li>Home</li><li>Services</li><li>Solutions</li><li>Resources</li><li>Career</li><li>Contact Us</li></ul>

  <h4 class="abs" style="left:890px">News letter</h4>
  <p class="abs news-text">Enter your email address for our mailing list to keep your self our lastest updated</p>
  <div class="abs field">Email</div>
  <div class="abs btn-red">Submit</div>
</footer>
<div class="abs base">Copyright © 2017 Dovin Pratchell Homes All Rights Reserved</div>

</body>
</html>
```